UX revamp for crypto platform mobile app

re-design the assets of a mobile app to give them a sleek, current and modern feel see reference below.
The current app has 3 main menus with subfunctions:
Wallet: Send - Receive - Top-up with shortcut to other main menus
Talents: User can support talent and see his support
Rewards: User can purchase rewards from Talents - Clubs - Vexmint

Target Market(s)

Youth fans of sports and entertainment

Industry/Entity Type

Blockchain

Colors

Designer to choose colors to be used in the design.

Requirements
Must have
• Modern - sleek - stylish - current trends design
Nice to have
• Need to be clean design
Should not have
• too dark and heavy

```html
<!DOCTYPE html>
<html lang="en">
<head>
<meta charset="utf-8">
<title>Profile – Vexmint</title>
<link href="https://fonts.googleapis.com/css2?family=Poppins:wght@300;400;500&family=Roboto:wght@400;500&display=swap" rel="stylesheet">
<style>
  :root {
    --page-bg: #f1f1f1;
    --screen-bg: #ffffff;
    --hero-bg: #f5f8fd;
    --hero-wave: #edf2fb;
    --ink: #2e2e33;
    --ink-soft: #8e8e95;
    --accent: #4f8ff7;
    --grad-a: #6a6ffd;
    --grad-b: #5aa0fb;
    --card-shadow: rgba(40, 60, 120, 0.08);
  }
  * { box-sizing: border-box; margin: 0; padding: 0; }
  html, body { width: 1200px; height: 1200px; overflow: hidden; }
  body { background: var(--page-bg); font-family: "Poppins", sans-serif; color: var(--ink); position: relative; }

  .screen {
    position: absolute; left: 413px; top: 113px; width: 375px; height: 974px;
    background: var(--screen-bg);
    box-shadow: 0 30px 50px rgba(0,0,0,0.06);
    overflow: hidden;
  }

  .status-bar {
    position: absolute; top: 0; left: 0; right: 0; height: 22px;
    font-family: "Roboto", sans-serif; font-size: 12px; color: #111;
  }
  .status-bar .signal { position: absolute; left: 6px; top: 5px; }
  .status-bar .time { position: absolute; left: 0; right: 0; top: 4px; text-align: center; }
  .status-bar .battery { position: absolute; right: 6px; top: 2px; display: flex; align-items: center; gap: 4px; font-size: 11px; }

  .hero {
    position: absolute; top: 0; left: 0; width: 375px; height: 329px;
    background: var(--hero-bg);
  }
  .hero-waves { position: absolute; left: 0; top: 0; }

  .nav-bar { position: absolute; top: 32px; left: 0; right: 0; height: 24px; }
  .nav-back { position: absolute; left: 15px; top: 3px; }
  .nav-title {
    position: absolute; left: 0; right: 0; top: 3px; text-align: center;
    font-size: 13px; font-weight: 400; letter-spacing: 2px; color: var(--accent);
  }
  .nav-more { position: absolute; right: 15px; top: 4px; }

  .avatar {
    position: absolute; left: 148px; top: 84px; width: 80px; height: 80px; border-radius: 50%;
    background: radial-gradient(circle at 50% 45%, #e8c7a4 0 30%, #d8b25c 45%, #4e6b2e 80%);
    border: 3px solid #fff;
    box-shadow: 0 6px 14px rgba(0,0,0,0.08);
  }

  .profile-name {
    position: absolute; left: 0; right: 0; top: 182px; text-align: center;
    font-size: 30px; font-weight: 400; color: var(--ink);
  }
  .profile-bio {
    position: absolute; left: 0; right: 0; top: 231px; text-align: center;
    font-size: 13.5px; font-weight: 300; line-height: 24px; color: var(--ink-soft);
  }
  .profile-actions {
    position: absolute; left: 0; right: 0; top: 290px; display: flex; justify-content: center; gap: 30px;
    font-size: 15px;
  }
  .profile-actions .follow { color: var(--accent); }
  .profile-actions .message { color: var(--ink); }

  .stats { position: absolute; left: 16px; top: 368px; width: 343px; list-style: none; }
  .stat-row { position: relative; height: 55px; margin-bottom: 25px; }
  .stat-row:nth-child(3) { margin-bottom: 26px; }
  .stat-card {
    position: absolute; left: 12px; right: 0; top: 0; height: 58px;
    background: #fff; box-shadow: 0 4px 10px var(--card-shadow);
  }
  .stat-icon {
    position: absolute; left: 0; top: 0; width: 62px; height: 55px;
    background: linear-gradient(135deg, var(--grad-a), var(--grad-b));
    display: flex; align-items: center; justify-content: center;
  }
  .stat-label { position: absolute; left: 82px; top: 17px; font-size: 15px; color: var(--ink); }
  .stat-value { position: absolute; right: 24px; top: 18px; font-size: 13.5px; font-weight: 300; color: var(--ink-soft); }

  .amount-field {
    position: absolute; left: 0; right: 0; top: 860px; height: 66px;
    text-align: center; line-height: 66px; font-size: 14px; font-weight: 300; color: var(--ink-soft);
  }
  .get-button {
    position: absolute; left: 0; right: 0; bottom: 0; height: 48px;
    background: linear-gradient(90deg, var(--grad-a), var(--grad-b));
    color: #fff; text-align: center; line-height: 48px; font-size: 14px; font-weight: 500; letter-spacing: 2px;
  }
</style>
</head>
<body>
<main class="screen">
  <section class="hero">
    <svg class="hero-waves" width="375" height="329" viewBox="0 0 375 329">
      <path d="M0 230 C40 170 90 150 150 158 C220 168 270 150 310 162 C340 170 360 140 375 130 L375 329 L0 329 Z" fill="var(--hero-wave)" opacity="0.7"/>
      <path d="M305 160 C340 130 360 90 375 60 L375 329 L300 329 Z" fill="#fff" opacity="0.6"/>
    </svg>
  </section>

  <div class="status-bar">
    <svg class="signal" width="30" height="10" viewBox="0 0 30 10">
      <rect x="0" y="6" width="2.5" height="3" fill="#111"/><rect x="3.5" y="4.5" width="2.5" height="4.5" fill="#111"/>
      <rect x="7" y="3" width="2.5" height="6" fill="#111"/><rect x="10.5" y="1.5" width="2.5" height="7.5" fill="#111"/>
      <path d="M16 3.5 Q21.5 -1 27 3.5 M18 5.5 Q21.5 2.5 25 5.5" stroke="#111" stroke-width="1.5" fill="none"/>
      <circle cx="21.5" cy="8" r="1.3" fill="#111"/>
    </svg>
    <div class="time">9:41 AM</div>
    <div class="battery">
      <svg width="6" height="10" viewBox="0 0 6 10"><path d="M0.5 2.5 L5 7 L3 9 V1 L5 3 L0.5 7.5" stroke="#111" fill="none"/></svg>
      <span>100%</span>
      <svg width="26" height="11" viewBox="0 0 26 11"><rect x="0.5" y="0.5" width="22" height="10" rx="2" fill="none" stroke="#111"/><rect x="2" y="2" width="19" height="7" rx="1" fill="#111"/><rect x="23.5" y="3.5" width="1.5" height="4" fill="#111"/></svg>
    </div>
  </div>

  <nav class="nav-bar">
    <svg class="nav-back" width="18" height="16" viewBox="0 0 18 16"><path d="M17 8 H2 M8 2 L2 8 L8 14" stroke="var(--accent)" stroke-width="1.8" fill="none" stroke-linecap="round"/></svg>
    <div class="nav-title">PROFILE</div>
    <svg class="nav-more" width="4" height="16" viewBox="0 0 4 16"><circle cx="2" cy="2" r="1.6" fill="var(--accent)"/><circle cx="2" cy="8" r="1.6" fill="var(--accent)"/><circle cx="2" cy="14" r="1.6" fill="var(--accent)"/></svg>
  </nav>

  <div class="avatar" role="img" aria-label="Profile photo of Lira Maddox"></div>
  <h1 class="profile-name">Lira Maddox</h1>
  <p class="profile-bio">Hi! My name is Lira,<br>I'm an actress from New York City.</p>
  <div class="profile-actions"><span class="follow">Follow</span><span class="message">Message</span></div>

  <ul class="stats">
    <li class="stat-row">
      <div class="stat-card"></div>
      <div class="stat-icon"><svg width="30" height="28" viewBox="0 0 30 28" fill="none" stroke="#fff" stroke-width="2.6" stroke-linecap="round" stroke-linejoin="round"><circle cx="20" cy="4" r="2.6" fill="#fff" stroke="none"/><path d="M11 9 L17 8 L14 16 L19 20 M14 16 L9 25 M17 8 L20 13 L25 13"/><path d="M1 6 H6 M2 10 H6 M3 14 H7"/></svg></div>
      <span class="stat-label">Field</span><span class="stat-value">Actress</span>
    </li>
    <li class="stat-row">
      <div class="stat-card"></div>
      <div class="stat-icon"><svg width="24" height="24" viewBox="0 0 24 24" fill="none" stroke="#fff" stroke-width="3.4" stroke-linecap="round" stroke-linejoin="round"><path d="M3 12 H20 M13 4 L21 12 L13 20"/></svg></div>
      <span class="stat-label">Released</span><span class="stat-value">0.000159%</span>
    </li>
    <li class="stat-row">
      <div class="stat-card"></div>
      <div class="stat-icon"><svg width="26" height="26" viewBox="0 0 24 24"><path d="M12 1.5 L15.1 8 L22 8.9 L17 13.7 L18.3 20.7 L12 17.3 L5.7 20.7 L7 13.7 L2 8.9 L8.9 8 Z" fill="#fff"/></svg></div>
      <span class="stat-label">USD Value</span><span class="stat-value">3500000.00</span>
    </li>
    <li class="stat-row">
      <div class="stat-card"></div>
      <div class="stat-icon"><svg width="34" height="34" viewBox="0 0 34 34"><circle cx="17" cy="17" r="15.5" fill="none" stroke="#fff" stroke-width="2"/><circle cx="17" cy="17" r="11" fill="#fff"/></svg></div>
      <span class="stat-label">VEX Value</span><span class="stat-value">128893979.18</span>
    </li>
    <li class="stat-row">
      <div class="stat-card"></div>
      <div class="stat-icon"><svg width="28" height="28" viewBox="0 0 28 28" fill="#fff"><path d="M2 3 H6.5 L10 17 H22 L25 8 H8.5 L7.8 5.5 H27.5 L23.5 19.5 H8.2 L4.8 5.5 H2 Z"/><circle cx="10" cy="24" r="2.2"/><circle cx="21" cy="24" r="2.2"/></svg></div>
      <span class="stat-label">VEX Commit</span><span class="stat-value">205.20</span>
    </li>
    <li class="stat-row">
      <div class="stat-card"></div>
      <div class="stat-icon"><svg width="28" height="22" viewBox="0 0 28 22" fill="none" stroke="#fff" stroke-width="4.2" stroke-linecap="round" stroke-linejoin="round"><path d="M3 11 L10.5 18 L25 3.5"/></svg></div>
      <span class="stat-label">Available</span><span class="stat-value">128893773.98</span>
    </li>
  </ul>

  <div class="amount-field">Enter Amount</div>
  <div class="get-button">GET</div>
</main>
</body>
</html>
```